依頼詳細
チラシに使用する文章と画像はこちらで用意いたします。
全体の雰囲気はimage2のような感じです。
記載項目
作りたいチラシのイメージはimage1のとおりです。
全体の雰囲気はimage2がイメージですが、デザインは自由に調整いただいてかまいません。
使用する色はimage2のような「水色・茶色」を考えておりますが、自由に調整いただいて結構です。
image1に犬のイラストがありますが、そちらも作成をお願いします。

使用する文章はPDFファイルを参照下さい。
image1のAからEはPDFファイルに記載しております。

image1の商品写真はimage_1の画像をご使用下さい。
image1の中身の写真はimage_2の画像をご使用下さい
サイズ
A4
ページ数
片面
希望イメージ
シンプル 複雑
単色 カラフル
暗い 明るい
日常 高級
遊び心 厳粛
未来的 伝統的
女性的 男性的
希望する色
水色 茶色
納品ファイル
• 高解像度JPG (.jpg)
• イラストレーター形式 (.ai)

```html
<!DOCTYPE html>
<html lang="ja">
<head>
<meta charset="utf-8">
<title>ペットのための無添加サプリ Lumiel</title>
<link rel="stylesheet" href="https://fonts.googleapis.com/css2?family=M+PLUS+Rounded+1c:wght@400;700;800&family=Kosugi+Maru&display=swap">
<style>
:root{
  --sky:#8fcfe6;
  --paper:#f3fafc;
  --brown:#6b3f1f;
  --navy:#1f4f7a;
  --heading-bar:#2f6f98;
  --ink:#3a3a3a;
  --orange:#e9963a;
  --white:#ffffff;
}
*{margin:0;padding:0;box-sizing:border-box}
html,body{width:849px;height:1200px;overflow:hidden}
body{font-family:"Kosugi Maru","M PLUS Rounded 1c",sans-serif;color:var(--ink);background:var(--sky)}
.flyer{position:relative;width:849px;height:1200px;background:var(--sky);overflow:hidden}
.top-area{position:absolute;left:0;top:0;width:849px;height:580px;background:var(--paper)}
.top-area::after{content:"";position:absolute;left:0;bottom:-1px;width:849px;height:70px;background:var(--sky);clip-path:ellipse(70% 100% at 50% 100%)}

.title-block{position:absolute;left:40px;top:48px;width:290px}
.title-ribbon{display:inline-block;background:var(--sky);color:var(--white);font-family:"M PLUS Rounded 1c",sans-serif;font-weight:800;font-size:24px;padding:8px 24px;border-radius:30px;transform:rotate(-6deg);border:3px solid var(--white);box-shadow:0 0 0 2px var(--sky)}
.title-box{margin-top:16px;border:4px solid var(--sky);border-radius:22px;background:var(--white);padding:18px 16px;text-align:center;color:var(--brown)}
.title-main{font-family:"M PLUS Rounded 1c",sans-serif;font-weight:800;font-size:38px;letter-spacing:2px;line-height:1.1}
.title-kana{font-size:13px;color:var(--brown);margin-top:6px}
.title-name{font-family:"M PLUS Rounded 1c",sans-serif;font-weight:800;font-size:48px;color:var(--brown);line-height:1.05;letter-spacing:3px}

.worries{position:absolute;left:465px;top:40px;width:355px}
.worries-head{font-family:"M PLUS Rounded 1c",sans-serif;font-weight:700;color:var(--brown);font-size:19px;line-height:1.4;display:flex;gap:10px;align-items:flex-start}
.worries-head svg{flex:none;margin-top:4px}
.worry-list{list-style:none;margin-top:10px}
.worry-list li{display:flex;align-items:center;gap:8px;font-size:14px;color:var(--ink);border-bottom:1px dashed var(--sky);padding:5px 0}
.worry-list li svg{flex:none}

.dog-art{position:absolute;left:520px;top:425px;width:290px;height:140px;background:linear-gradient(180deg,#7a4a24,#5a3416);border-radius:70px 70px 24px 24px;z-index:2}

.info{position:absolute;top:600px;width:380px}
.info.left{left:30px}.info.right{left:440px}
.info-head{display:flex;align-items:center;gap:8px;background:var(--heading-bar);color:var(--white);font-family:"M PLUS Rounded 1c",sans-serif;font-weight:700;font-size:16px;padding:6px 14px;border-radius:6px}
.info-text{margin-top:10px;font-size:12.5px;line-height:1.75;color:var(--white)}

.feature{position:absolute;left:30px;top:800px;width:789px;height:365px;background:var(--white);border-radius:20px;padding:18px 24px}
.feature-head{display:flex;align-items:center;gap:10px;font-family:"M PLUS Rounded 1c",sans-serif;font-weight:800;color:var(--navy);font-size:21px;border-bottom:3px solid var(--sky);padding-bottom:8px}
.feature-body{display:grid;grid-template-columns:240px 220px 1fr;gap:22px;margin-top:16px}
.feature-text{font-size:12px;line-height:1.75;color:var(--ink)}
.product-photo{height:160px;border-radius:10px;background:linear-gradient(160deg,#f2f2ee,#dfe6e2)}
.content-photo{height:90px;width:130px;margin:12px auto 0;border-radius:50%;background:radial-gradient(circle,#e8c27a,#c8934a)}
.points-head{display:inline-block;background:var(--orange);color:var(--white);font-weight:700;font-size:13px;padding:2px 12px;border-radius:12px;margin-bottom:6px}
.spec{list-style:none;margin-top:6px;font-size:12px;line-height:1.75}
</style>
</head>
<body>
<main class="flyer">
  <section class="top-area">
    <div class="title-block">
      <span class="title-ribbon">ペットのための</span>
      <div class="title-box">
        <p class="title-main">無添加<br>サプリ</p>
        <p class="title-kana">ルミエル</p>
        <p class="title-name">Lumiel</p>
      </div>
    </div>

    <div class="worries">
      <h2 class="worries-head">
        <svg width="26" height="26" viewBox="0 0 26 26"><circle cx="13" cy="13" r="12" fill="var(--brown)"/></svg>
        <span>こんなことに<br>お悩みではないですか？</span>
      </h2>
      <ul class="worry-list">
        <li><svg width="16" height="16" viewBox="0 0 16 16"><rect x="1" y="1" width="14" height="14" rx="2" fill="none" stroke="var(--brown)" stroke-width="1.6"/><path d="M4 8l3 3 5-6" fill="none" stroke="var(--orange)" stroke-width="2"/></svg>フードの食いつきが悪い</li>
        <li><svg width="16" height="16" viewBox="0 0 16 16"><rect x="1" y="1" width="14" height="14" rx="2" fill="none" stroke="var(--brown)" stroke-width="1.6"/><path d="M4 8l3 3 5-6" fill="none" stroke="var(--orange)" stroke-width="2"/></svg>食が細い</li>
        <li><svg width="16" height="16" viewBox="0 0 16 16"><rect x="1" y="1" width="14" height="14" rx="2" fill="none" stroke="var(--brown)" stroke-width="1.6"/><path d="M4 8l3 3 5-6" fill="none" stroke="var(--orange)" stroke-width="2"/></svg>シニア・子犬・子猫に栄養を取らせたい</li>
        <li><svg width="16" height="16" viewBox="0 0 16 16"><rect x="1" y="1" width="14" height="14" rx="2" fill="none" stroke="var(--brown)" stroke-width="1.6"/><path d="M4 8l3 3 5-6" fill="none" stroke="var(--orange)" stroke-width="2"/></svg>手術後の回復を早めたい</li>
        <li><svg width="16" height="16" viewBox="0 0 16 16"><rect x="1" y="1" width="14" height="14" rx="2" fill="none" stroke="var(--brown)" stroke-width="1.6"/><path d="M4 8l3 3 5-6" fill="none" stroke="var(--orange)" stroke-width="2"/></svg>妊娠中の栄養が心配だ</li>
        <li><svg width="16" height="16" viewBox="0 0 16 16"><rect x="1" y="1" width="14" height="14" rx="2" fill="none" stroke="var(--brown)" stroke-width="1.6"/><path d="M4 8l3 3 5-6" fill="none" stroke="var(--orange)" stroke-width="2"/></svg>アトピーやアレルギーをもっている</li>
        <li><svg width="16" height="16" viewBox="0 0 16 16"><rect x="1" y="1" width="14" height="14" rx="2" fill="none" stroke="var(--brown)" stroke-width="1.6"/><path d="M4 8l3 3 5-6" fill="none" stroke="var(--orange)" stroke-width="2"/></svg>免疫力を高めたい</li>
        <li><svg width="16" height="16" viewBox="0 0 16 16"><rect x="1" y="1" width="14" height="14" rx="2" fill="none" stroke="var(--brown)" stroke-width="1.6"/><path d="M4 8l3 3 5-6" fill="none" stroke="var(--orange)" stroke-width="2"/></svg>生活習慣病を予防したい</li>
        <li><svg width="16" height="16" viewBox="0 0 16 16"><rect x="1" y="1" width="14" height="14" rx="2" fill="none" stroke="var(--brown)" stroke-width="1.6"/><path d="M4 8l3 3 5-6" fill="none" stroke="var(--orange)" stroke-width="2"/></svg>下部尿路系疾患が心配だ</li>
      </ul>
    </div>
  </section>

  <div class="dog-art" role="img" aria-label="横向きに立つ茶色のダックスフンドのイラスト"></div>

  <section class="info left">
    <h3 class="info-head"><svg width="16" height="16" viewBox="0 0 16 16"><circle cx="8" cy="8" r="7" fill="var(--white)"/></svg>増え続けるペットの生活習慣病</h3>
    <p class="info-text">食生活の変化や運動不足により、ペットの生活習慣病は年々増えています。肥満や糖尿病、心臓病などは人間と同じように、毎日の積み重ねが原因となります。早めの対策で、大切な家族の健康を守りましょう。</p>
  </section>

  <section class="info right">
    <h3 class="info-head"><svg width="16" height="16" viewBox="0 0 16 16"><circle cx="8" cy="8" r="7" fill="var(--white)"/></svg>予防するためには</h3>
    <p class="info-text">青魚に多く含まれる「DHA」や「EPA」は、生活習慣病の予防に役立つといわれています。血液の流れを整え、体の内側から健康をサポートします。毎日のフードに加えるだけで、無理なく続けられます。</p>
  </section>

  <section class="feature">
    <h2 class="feature-head"><svg width="26" height="26" viewBox="0 0 26 26"><circle cx="13" cy="13" r="12" fill="var(--sky)"/></svg>Lumiel（ルミエル）で生活習慣病を撃退！</h2>
    <div class="feature-body">
      <p class="feature-text">LumielはDHAやEPAを豊富に含む青魚を原料にしています。一般的なペットフードには不足しがちな栄養素を、毎日手軽に補うことができます。保存料や着色料は一切使用せず、素材そのものの味を大切にしました。食いつきが良いので、食の細い子やシニアの子にも安心してお使いいただけます。</p>
      <div>
        <div class="product-photo" role="img" aria-label="サプリメントの商品パッケージ写真"></div>
        <div class="content-photo" role="img" aria-label="小皿に入ったサプリメントの中身の写真"></div>
      </div>
      <div class="feature-text">
        <span class="points-head">特徴</span>
        <p>Lumielは、食べやすいふりかけタイプのサプリメントです。いつものフードにかけるだけで、無理なく続けられます。体重に合わせて量を調整できます。</p>
        <ul class="spec">
          <li>原材料：青魚・植物油</li>
          <li>内容量：90g</li>
          <li>価格：2,980円（税込）</li>
          <li>与え方：1日1〜2回</li>
        </ul>
      </div>
    </div>
  </section>
</main>
</body>
</html>
```